TalkBridge - Language Coaching Services

Sleek, innovative, trendy design for Language Coaching business.

TalkBridge is a new UK based company that provides Language Coaching services. We offer highly personalized on-line and face to face language courses. We also impart learning techniques workshops based on the latest neuroscience research for second-language acquisition.

Target Market(s)

Industry/Entity Type

Consulting

Contact Information for Business Card

TalkBridge
ElenaVT@talkbridge-demo.co.uk
TalkBridge-demo.co.uk
London, UK

Font styles to use
Sans Serif

```html
<!DOCTYPE html>
<html lang="en">
<head>
<meta charset="utf-8">
<title>TalkBridge Business Card</title>
<link rel="stylesheet" href="https://fonts.googleapis.com/css2?family=Montserrat:wght@400&family=Josefin+Sans:wght@600;700&family=Noto+Serif:wght@700&display=swap">
<style>
  :root {
    --stage: #e6e6e6;
    --brand-blue: #2289b0;
    --ink: #1b1b1b;
    --paper: #ffffff;
  }
  html, body {
    margin: 0;
    padding: 0;
    overflow: hidden;
    background: var(--paper);
  }
  .stage {
    position: relative;
    width: 1200px;
    height: 990px;
    background: var(--stage);
    border-radius: 34px;
    overflow: hidden;
  }
  .card {
    position: absolute;
    top: 214px;
    width: 337px;
    height: 546px;
  }
  .card--front { left: 228px; }
  .card--back { left: 614px; }
  .card svg { display: block; width: 100%; height: 100%; }
  .brand-name {
    font-family: "Montserrat", sans-serif;
    font-weight: 400;
    letter-spacing: 1px;
  }
  .web-address, .contact-line {
    font-family: "Noto Serif", serif;
    font-weight: 700;
  }
  .person-name {
    font-family: "Josefin Sans", sans-serif;
    font-weight: 700;
  }
  .person-title {
    font-family: "Josefin Sans", sans-serif;
    font-weight: 600;
  }
</style>
</head>
<body>
<main class="stage">

  <section class="card card--front" aria-label="Card front">
    <svg viewBox="0 0 397 643" xmlns="http://www.w3.org/2000/svg">
      <rect class="front-band" width="397" height="643" fill="var(--brand-blue)"/>
      <polygon class="front-arrow" points="75,0 322,0 322,353 198,598 75,353" fill="var(--paper)"/>
      <polygon class="front-base" points="0,422 198,598 397,422 397,643 0,643" fill="var(--ink)"/>
      <circle class="brand-dot" cx="198" cy="186" r="40" fill="none" stroke="var(--brand-blue)" stroke-width="6"/>
      <text class="brand-name" x="198" y="264" text-anchor="middle" font-size="30" fill="var(--brand-blue)">TALKBRIDGE</text>
      <text class="web-address" x="198" y="624" text-anchor="middle" font-size="15" fill="var(--paper)">talkbridge-demo.co.uk</text>
    </svg>
  </section>

  <section class="card card--back" aria-label="Card back">
    <svg viewBox="0 0 397 643" xmlns="http://www.w3.org/2000/svg">
      <rect class="back-base" width="397" height="643" fill="var(--ink)"/>
      <polygon class="back-panel" points="0,167 198,342 397,167 397,422 198,598 0,422" fill="var(--paper)"/>
      <polygon class="back-band" points="75,0 322,0 322,200 310,215 397,167 198,342 0,167 87,215 75,200" fill="var(--brand-blue)"/>
      <circle class="brand-dot" cx="198" cy="103" r="32" fill="none" stroke="var(--paper)" stroke-width="4"/>
      <text class="brand-name" x="198" y="164" text-anchor="middle" font-size="23" fill="var(--paper)">TALKBRIDGE</text>
      <text class="person-name" x="200" y="378" text-anchor="middle" font-size="34" fill="#000">HARRIET</text>
      <text class="person-title" x="200" y="394" text-anchor="middle" font-size="12" fill="#000">GRAND MANAGER</text>
      <text class="contact-line" x="204" y="448" text-anchor="middle" font-size="11" fill="#000">020 - 555 - 0142</text>
      <text class="contact-line" x="204" y="477" text-anchor="middle" font-size="11" fill="#000">info@talkbridge-demo.co.uk</text>
      <text class="contact-line" x="204" y="503" text-anchor="middle" font-size="9" fill="#000">Riverside House, Unit 4</text>
      <text class="contact-line" x="204" y="516" text-anchor="middle" font-size="9" fill="#000">London, UK</text>
      <text class="web-address" x="198" y="624" text-anchor="middle" font-size="15" fill="var(--paper)">talkbridge-demo.co.uk</text>
    </svg>
  </section>

</main>
</body>
</html>
```